Website Design for new skincare product launch/rebranding

The Dew Meridian website is currently live and built through Pagevolt.com. While the existing site has served as a strong starting point, I’m now looking to elevate the overall experience with a complete redesign that reflects the growth and vision of the brand. This will be a full visual and functional revamp — not just a refresh — with the goal of creating a more elevated, intuitive, and conversion-focused platform. I’m looking for a designer who can not only reimagine the layout and visuals, but also collaborate on optimizing the user journey and site structure for both storytelling and sales.

Target Market(s)

Age 25- 45 (core), with secondary appeal to 18-55. Primarily women, but gender inclusive. Wellness/Holistic Beauty/Organic Ingredients, Botanical.

Industry/Entity Type

Beauty, aesthetics, wellness.

Number of Pages Required

5+ page

Font styles to use
Other font styles liked:
• Gravesned Sans Family

Colors

Designer to choose colors to be used in the design.

Requirements
Must have
• Include standard pages (Home, Our Story/Values, Shop, Product Detail with ingredients/description/etc., Contact) and any other recommended sections to optimize conversion. Minimal, clean, calming visual. Seamlessly integrate with Cartwell for all product sales.
Nice to have
• Company colors are attached in images, along with first two products that are launching. One called Velunmist, and one called Petravelle. Fonts and shapes need to align accordingly. Feel elevated, neutral, and luxe while maintaining a grounded, earthy minimalism. Visual inspiration includes brands like Lantern Grove, Marble Osprey, and TOvelin — minimal yet high-end, with thoughtful use of whitespace, typography, and subtle movement. Would LOVE to have movement (short clip GIF) on either the home page or ingredient page, reference TOvelin website (homepage or LuminWeave System™ Tab)
Should not have
• dark colors, complex design elements, too many different fonts. For ingredients, stick to botanical images and information only, with no mentions of CBD or use of leaf imagery.

```html
<!DOCTYPE html>
<html lang="en">
<head>
<meta charset="utf-8">
<title>Dew Meridian — Home</title>
<link rel="stylesheet" href="https://fonts.googleapis.com/css2?family=Didact+Gothic&family=Poppins:wght@400;500&family=Cormorant+Garamond:ital,wght@1,500&display=swap">
<style>
:root{
  --ink:#3b3b3b;
  --muted:#5a5a5a;
  --logo:#c9bdb8;
  --button:#dccfcb;
  --button-dark:#8b8b86;
  --panel:#f4f2ef;
  --band:#f0efed;
  --signup:#c6c7c2;
  --line:#d9d9d9;
  --mint:#9fcfba;
  --lavender:#a79dd0;
  --blush:#d3c8c5;
  --white:#ffffff;
}
*{box-sizing:border-box;margin:0;padding:0}
html,body{width:1200px;height:4577px;overflow:hidden}
body{position:relative;background:var(--white);color:var(--ink);font-family:"Didact Gothic",sans-serif}
.abs{position:absolute}
.btn{position:absolute;display:flex;align-items:center;justify-content:center;background:var(--button);color:var(--ink);font-size:18px;letter-spacing:.5px}
.btn--dark{background:var(--button-dark);color:var(--white)}

/* header */
.topbar{left:0;top:0;width:1200px;height:68px;border-bottom:1px solid var(--line)}
.topbar__note{left:76px;top:28px;font-family:"Poppins",sans-serif;font-size:12px;color:#222}
.social{top:28px;width:13px;height:13px;border-radius:2px;background:#333}
.logo{left:476px;top:0;width:248px;height:148px;background:var(--white);display:flex;align-items:flex-end;justify-content:center;padding-bottom:36px;font-size:30px;color:var(--logo);letter-spacing:1px;white-space:nowrap}
.nav a{position:absolute;top:96px;font-size:16px;color:var(--ink);text-decoration:none}
.nav a.is-active{text-decoration:underline;text-underline-offset:5px}

/* hero */
.hero__photo{left:0;top:148px;width:1200px;height:572px;clip-path:polygon(458px 0,1200px 0,1200px 572px,516px 572px,482px 330px);background:linear-gradient(120deg,#d8d6d2 0%,#e6c9b4 45%,#d9b394 70%,#cfd4d2 100%)}
.hero__title{left:78px;top:266px;font-size:58px;line-height:57px;letter-spacing:2.4px;font-weight:400}
.hero__sub{left:73px;top:448px;font-size:25px;line-height:34px;letter-spacing:.6px}

/* about */
.center{left:0;width:1200px;text-align:center}
.about__eyebrow{top:798px;font-size:36px;letter-spacing:1.5px}
.about__title{top:842px;font-size:50px;letter-spacing:2px}
.about__text{left:172px;top:929px;width:856px;text-align:center;font-size:17.5px;line-height:31px;letter-spacing:.9px}

/* arrivals */
.arrival{top:1239px;width:596px;height:516px;background:var(--panel)}
.arrival__eyebrow{font-size:23px;letter-spacing:1.2px}
.arrival__name{font-size:30px;letter-spacing:1.6px}
.arrival__price{font-size:21px}
.product{border-radius:20px 20px 10px 10px}

/* shop */
.shop__title{top:1828px;font-size:50px;letter-spacing:2px}
.card{top:1929px;width:329px;height:249px;border-radius:10px;overflow:hidden}
.card__name{font-size:30px;color:var(--white);letter-spacing:.8px}
.card__price{font-size:21px;color:var(--white)}
.card__link{font-size:15px;color:var(--white);text-decoration:underline}

/* why */
.why{left:0;top:2270px;width:1200px;height:642px;background:var(--band)}
.why__eyebrow{left:96px;top:2320px;font-size:39px;letter-spacing:1.8px}
.why__title{left:96px;top:2362px;font-size:50px;letter-spacing:3.5px}
.why__item{left:636px;font-size:21px;letter-spacing:.8px;display:flex;align-items:center;gap:10px}

/* founder */
.founder__hi{left:121px;top:3040px;font-family:"Cormorant Garamond",serif;font-style:italic;font-weight:500;font-size:40px;letter-spacing:1px}
.founder__role{left:121px;top:3092px;font-size:25px;line-height:33px;letter-spacing:2.2px;text-transform:uppercase}
.founder__text{left:122px;top:3178px;width:500px;font-size:17.5px;line-height:30.5px;letter-spacing:.8px}
.founder__photo{left:681px;top:2987px;width:387px;height:433px;border-radius:194px 194px 0 0;background:linear-gradient(180deg,#e8e7e4 0%,#e0cbb6 45%,#f3eee8 100%)}

/* signup */
.signup{left:0;top:3524px;width:1200px;height:337px;background:var(--signup)}
.signup__title{top:3605px;font-size:39px;letter-spacing:2.5px}
.signup__sub{top:3659px;font-size:25px;letter-spacing:1.5px}
.signup__input{left:208px;top:3721px;width:603px;height:48px;background:var(--white);border:1px solid #aaa;font-family:"Poppins",sans-serif;font-size:12px;color:#333;padding:16px 18px}
.signup__btn{left:825px;top:3721px;width:165px;height:48px;border:1px solid var(--white);color:#333;font-size:17px;letter-spacing:1.5px;display:flex;align-items:center;justify-content:center}

/* social feed */
.feed__handle{top:3922px;font-size:28px;letter-spacing:1.2px}
.feed__tile{top:3986px;height:169px;border-radius:6px}
.feed__track{left:0;top:4200px;width:1200px;height:1px;background:var(--line)}
.feed__thumb{left:75px;top:4198px;width:163px;height:5px;background:#b9b9b9}

/* footer */
.footer{left:0;top:4263px;width:1200px;height:314px;background:var(--band)}
.footer__col{top:4322px;width:300px;text-align:center}
.footer__head{font-size:23px;letter-spacing:1.5px;margin-bottom:10px}
.footer__col a{display:block;font-size:17px;line-height:35px;color:var(--ink);text-decoration:none}
.footer__logo{top:4378px;font-size:34px;color:var(--logo);letter-spacing:1px}
.footer__copy{top:4448px;font-family:"Poppins",sans-serif;font-size:13px;line-height:25px}
</style>
</head>
<body>

<!-- header -->
<div class="abs topbar"></div>
<div class="abs topbar__note">Free Shipping On Orders Over $50</div>
<span class="abs social" style="left:1073px" role="img" aria-label="Social profile"></span>
<span class="abs social" style="left:1112px;border-radius:50%" role="img" aria-label="Social profile"></span>
<div class="abs logo">DEW MERIDIAN</div>
<nav class="nav">
  <a class="is-active" href="#" style="left:124px">Home</a>
  <a href="#" style="left:218px">Our Story</a>
  <a href="#" style="left:345px">Shop</a>
  <a href="#" style="left:790px">Products</a>
  <a href="#" style="left:908px">Contact</a>
</nav>
<svg class="abs" style="left:1018px;top:98px" width="18" height="18" viewBox="0 0 18 18" aria-label="Account"><circle cx="9" cy="9" r="7.5" fill="none" stroke="#333" stroke-width="1.6"/><circle cx="9" cy="7.5" r="2.5" fill="none" stroke="#333" stroke-width="1.5"/><path d="M4.5 14c1.5-2.5 7.5-2.5 9 0" fill="none" stroke="#333" stroke-width="1.5"/></svg>
<svg class="abs" style="left:1061px;top:97px" width="16" height="18" viewBox="0 0 16 18" aria-label="Bag"><path d="M5 6V4a3 3 0 0 1 6 0v2" fill="none" stroke="#333" stroke-width="1.6"/><rect x="1" y="6" width="14" height="11" rx="2" fill="#333"/></svg>

<!-- hero -->
<div class="abs hero__photo" role="img" aria-label="Smiling woman applying a mint facial balm stick to her cheek"></div>
<h1 class="abs hero__title" style="font-weight:400">Bring Home<br>The Treatment<br>Room</h1>
<p class="abs hero__sub">Total Dewfall mini facial kit<br>post-facial glow included!</p>
<a class="btn" style="left:75px;top:537px;width:185px;height:52px">Shop Now</a>

<!-- about -->
<div class="abs center about__eyebrow">About Us</div>
<h2 class="abs center about__title" style="font-weight:400">Our Story</h2>
<p class="abs about__text">Nemo enim ipsam voluptatem quia voluptas sit aspernatur aut odit aut fugit, sed quia consequuntur magni dolores eos qui ratione voluptatem sequi nesciunt. Neque porro quisquam est, qui dolorem ipsum quia dolor sit amet, consectetur, adipisci velit, sed quia non numquam eius modi tempora incidunt ut labore et dolore magnam</p>
<a class="btn" style="left:507px;top:1093px;width:185px;height:54px">Read More</a>

<!-- new arrivals -->
<section class="abs arrival" style="left:0">
  <div class="abs arrival__eyebrow" style="left:75px;top:168px">New Arrivals</div>
  <div class="abs arrival__name" style="left:75px;top:196px">Botanical Serum</div>
  <div class="abs arrival__price" style="left:75px;top:243px">$45</div>
  <a class="btn btn--dark" style="left:75px;top:290px;width:163px;height:51px">Shop Now</a>
  <div class="abs product" style="left:368px;top:68px;width:156px;height:382px;background:linear-gradient(180deg,#ededec 0%,#dcdcdb 30%,#a9a9a8 45%,#8f8f8e 100%)" role="img" aria-label="Velunmist botanical serum dropper bottle"></div>
</section>
<section class="abs arrival" style="left:604px">
  <div class="abs arrival__eyebrow" style="left:43px;top:168px">New Arrivals</div>
  <div class="abs arrival__name" style="left:43px;top:196px">Botanical Balm</div>
  <div class="abs arrival__price" style="left:43px;top:243px">$45</div>
  <a class="btn" style="left:43px;top:290px;width:165px;height:51px">Shop Now</a>
  <div class="abs product" style="left:331px;top:65px;width:158px;height:382px;border-radius:14px;background:linear-gradient(90deg,#d9d8de 0%,#f6f6f8 45%,#dedde3 100%)" role="img" aria-label="Petravelle botanical balm stick"></div>
</section>

<!-- shop -->
<h2 class="abs center shop__title" style="font-weight:400">Shop</h2>
<div class="abs card" style="left:75px;background:var(--mint)">
  <div class="abs" style="left:22px;top:30px;width:150px;height:210px;background:linear-gradient(90deg,#e3efe9,#c4e1d4)" role="img" aria-label="Sol.calm product boxes"></div>
  <div class="abs card__name" style="left:190px;top:86px">sol.calm</div>
  <div class="abs card__price" style="left:192px;top:132px">$45</div>
  <div class="abs card__link" style="left:192px;top:167px">Shop Now</div>
</div>
<div class="abs card" style="left:436px;background:var(--lavender)">
  <div class="abs" style="left:25px;top:22px;width:140px;height:210px;background:linear-gradient(180deg,#efe3a4 0%,#eeeaf4 22%,#d9d3ea 100%)" role="img" aria-label="Lune.dew balm stick and jar"></div>
  <div class="abs card__name" style="left:182px;top:86px">lune.dew</div>
  <div class="abs card__price" style="left:183px;top:132px">$45</div>
</div>
<div class="abs card" style="left:798px;background:var(--blush)">
  <div class="abs" style="left:22px;top:20px;width:150px;height:215px;background:linear-gradient(180deg,#e6e6e6 0%,#b3b3b3 45%,#9a9a9a 100%);border-radius:14px" role="img" aria-label="Two serum dropper bottles"></div>
  <div class="abs card__name" style="left:203px;top:86px">Serum</div>
  <div class="abs card__price" style="left:205px;top:132px">$45</div>
</div>

<!-- why -->
<section class="abs why"></section>
<div class="abs why__eyebrow">Why See Products</div>
<h2 class="abs why__title" style="font-weight:400">DEW MERIDIAN?</h2>
<div class="abs" style="left:156px;top:2453px;width:292px;height:374px;border-radius:18px;background:linear-gradient(90deg,#a3a3a3 0%,#c7c7c7 40%,#ecebef 60%,#dcdbe1 100%)" role="img" aria-label="Serum bottle beside balm stick"></div>
<div class="abs why__item" style="top:2405px"><svg width="20" height="16" viewBox="0 0 20 16"><path d="M2 8l5 5L18 2" fill="none" stroke="#7a7a7a" stroke-width="3"/></svg>Clean, Natural, Organically Sourced</div>
<div class="abs why__item" style="top:2472px"><svg width="20" height="16" viewBox="0 0 20 16"><path d="M2 8l5 5L18 2" fill="none" stroke="#7a7a7a" stroke-width="3"/></svg>Less than Ten Ingredients</div>
<div class="abs why__item" style="top:2540px"><svg width="20" height="16" viewBox="0 0 20 16"><path d="M2 8l5 5L18 2" fill="none" stroke="#7a7a7a" stroke-width="3"/></svg>Completely Recyclable</div>
<div class="abs why__item" style="top:2607px"><svg width="20" height="16" viewBox="0 0 20 16"><path d="M2 8l5 5L18 2" fill="none" stroke="#7a7a7a" stroke-width="3"/></svg>Proven Skin Transformation by Clients</div>
<div class="abs why__item" style="top:2675px"><svg width="20" height="16" viewBox="0 0 20 16"><path d="M2 8l5 5L18 2" fill="none" stroke="#7a7a7a" stroke-width="3"/></svg>Use on Any Age, Any Race, Any Body (part)</div>
<a class="btn" style="left:636px;top:2754px;width:185px;height:53px">See Products</a>

<!-- founder -->
<div class="abs founder__hi">Hi, I'm Maren!</div>
<div class="abs founder__role">Medical Esthetician &amp; Creator<br>of Dew Meridian</div>
<p class="abs founder__text">My goal is to empower people beyond my treatment room to elevate their skin + honor their self  with intentional &amp; effective products that deliver those coveted post-facial results each and every day.</p>
<a class="btn" style="left:122px;top:3342px;width:186px;height:54px">Read More</a>
<div class="abs founder__photo" role="img" aria-label="Portrait of the founder, smiling, in a cream blouse"></div>

<!-- signup -->
<section class="abs signup"></section>
<div class="abs center signup__title">I Am Dewy</div>
<div class="abs center signup__sub">Sign Up for Emails &amp; Get 10% Off Your First Purchase</div>
<div class="abs signup__input">Enter Email Address</div>
<div class="abs signup__btn">SUBSCRIBE</div>

<!-- feed -->
<div class="abs center feed__handle">@Dew Meridian</div>
<div class="abs feed__tile" style="left:0;width:208px;border-radius:0 6px 6px 0;background:linear-gradient(135deg,#d9b89c,#b9c9b6)" role="img" aria-label="Woman using a facial roller"></div>
<div class="abs feed__tile" style="left:213px;width:255px;background:var(--mint)" role="img" aria-label="Product boxes on mint background"></div>
<div class="abs feed__tile" style="left:475px;width:254px;background:linear-gradient(135deg,#cfd1cf,#e0c2a8)" role="img" aria-label="Smiling woman with balm stick"></div>
<div class="abs feed__tile" style="left:734px;width:254px;background:var(--lavender)" role="img" aria-label="Hand holding a balm stick"></div>
<div class="abs feed__tile" style="left:996px;width:204px;border-radius:6px 0 0 6px;background:linear-gradient(90deg,#f1f1f1,#c8c8c8)" role="img" aria-label="Serum bottle on white"></div>
<div class="abs feed__track"></div>
<div class="abs feed__thumb"></div>

<!-- footer -->
<footer class="abs footer"></footer>
<div class="abs footer__col" style="left:101px">
  <div class="footer__head">QUICK LINKS</div>
  <a href="#">Home</a><a href="#">Our Story</a><a href="#">Shop</a><a href="#">Products</a><a href="#">Contact</a>
</div>
<div class="abs center footer__logo">DEW MERIDIAN</div>
<div class="abs center footer__copy">Copyright © 2025. Company Name<br>All Right Reserved</div>
<span class="abs social" style="left:573px;top:4503px;width:11px;height:11px;background:#888" role="img" aria-label="Social profile"></span>
<span class="abs social" style="left:613px;top:4503px;width:11px;height:11px;border-radius:50%;background:#888" role="img" aria-label="Social profile"></span>
<div class="abs footer__col" style="left:801px">
  <div class="footer__head">LEGAL</div>
  <a href="#">FAQ</a><a href="#">Privacy Policy</a><a href="#">Shipping + Returns</a><a href="#">Terms AND Conditions</a>
</div>

</body>
</html>
```